Awesome Web Design Project

must have a link to palsphere of the homepage preferably a scrolling view of our palsphere page!

We are an exciting new electrical company with a strong focus on energy efficiency and offering the latest technologies.

The design should allow easy navigation, there shouldn't be too many menus, It should look clean and sleek, Colours to consider could be green, silver/chrome, black,

The site should convey technology, efficiency and simplicity

Must be viewable on all devices, pc's, tablets, phones ie Responsive

Logo and some pics uploaded!

Industry/Entity Type

Electrical

Requirements
Must have
• must include the following pages,
about us
our services
gallery
contact us
Connect with us
Nice to have
• Would be great if the website design used a user friendly cms,
Should not have
• too many links, menus, clutter it should be clean and easy to navigate

```html
<!DOCTYPE html>
<html lang="en">
<head>
<meta charset="utf-8">
<title>Kestrel Electrical – Home</title>
<link href="https://fonts.googleapis.com/css2?family=Cabin:wght@400;500&family=Montserrat:wght@300;800&display=swap" rel="stylesheet">
<style>
:root{
  --teal-dark:#0f3d42;
  --teal:#1e4d52;
  --teal-light:#2f6166;
  --lime:#d6e02c;
  --page:#f1f1f1;
  --header:#ececec;
  --ink:#0a0a0a;
  --footer-top:#3b3e41;
  --footer-bottom:#1c1e20;
  --white:#ffffff;
}
*{margin:0;padding:0;box-sizing:border-box}
html,body{width:1200px;height:878px;overflow:hidden}
body{position:relative;background:var(--page);font-family:"Cabin",sans-serif;color:var(--teal-dark)}
a{color:inherit;text-decoration:none}

.site-header{position:absolute;left:0;top:0;width:1200px;height:157px;
  background:linear-gradient(180deg,#fafafa 0,var(--header) 100%);border-top:0}
.site-header::before{content:"";position:absolute;left:0;right:0;top:39px;height:1px;background:#d7d7d7}

.brand{position:absolute;left:185px;top:66px;display:flex;align-items:center;gap:14px}
.brand-mark{width:46px;height:46px;background:var(--lime)}
.brand-name{font-family:"Cabin",sans-serif;font-weight:500;font-size:38px;letter-spacing:3px;color:var(--teal);text-transform:uppercase}

.connect{position:absolute;left:758px;top:29px;width:246px;height:38px;background:var(--teal-dark);
  display:flex;align-items:center;justify-content:space-between;padding:0 13px 0 19px;color:var(--white);font-size:17px}
.connect::before,.connect::after{content:"";position:absolute;top:0;width:0;height:0;border-style:solid}
.connect::before{left:-12px;border-width:0 12px 9px 0;border-color:transparent var(--ink) transparent transparent}
.connect::after{right:-12px;border-width:0 0 9px 12px;border-color:transparent transparent transparent var(--ink)}
.connect-dot{width:26px;height:26px;border-radius:50%;background:var(--lime)}

.search{position:absolute;left:758px;top:86px;width:246px;height:35px;background:var(--ink);display:flex;align-items:center}
.search-field{flex:1;padding-left:18px;font-size:12px;color:#d0d0d0;border-right:1px solid #3a3a3a;height:21px;line-height:21px}
.search-button{width:40px;display:flex;justify-content:center}

.main-nav{position:absolute;left:0;top:157px;width:1200px;height:40px;
  background:repeating-linear-gradient(45deg,rgba(255,255,255,.04) 0 1px,transparent 1px 3px),
  linear-gradient(180deg,var(--teal-light),#163b3f)}
.main-nav a{position:absolute;top:0;height:40px;line-height:40px;font-size:19px;color:var(--white);letter-spacing:-.3px}
.main-nav .current{left:185px;width:102px;height:56px;line-height:60px;text-align:center;background:var(--lime);color:var(--teal-dark)}
.nav-sep{position:absolute;top:8px;width:1px;height:24px;background:rgba(255,255,255,.2)}

.headline{position:absolute;left:182px;top:226px;font-family:"Montserrat",sans-serif;font-size:45px;letter-spacing:-1px;color:var(--teal-dark);white-space:nowrap}
.headline .light{font-weight:300}
.headline strong{font-weight:800}

.hero{position:absolute;left:172px;top:289px;width:857px;height:272px;
  background:linear-gradient(180deg,#a9abad 0,#8d9093 40%,#5d6164 100%)}

.feature{position:absolute;top:583px;width:210px;height:169px;overflow:hidden;box-shadow:0 3px 5px rgba(0,0,0,.2)}
.feature-photo{position:absolute;left:0;width:100%}
.feature-caption{position:absolute;left:0;width:100%;background:var(--teal);color:var(--white);font-size:17px;line-height:19px;padding:0 14px;display:flex;align-items:center}
.feature-title{position:absolute;left:0;top:0;width:100%;height:50px;background:var(--lime);color:var(--teal-dark);font-size:17px;padding:0 16px;display:flex;align-items:center}
.play{position:absolute;width:21px;height:21px;border-radius:50%;background:#f4f4f4;display:flex;align-items:center;justify-content:center}
.play::after{content:"";border-style:solid;border-width:4px 0 4px 7px;border-color:transparent transparent transparent #333;margin-left:2px}

.site-footer{position:absolute;left:0;top:794px;width:1200px;height:84px;background:linear-gradient(180deg,var(--footer-top),var(--footer-bottom));border-top:1px solid #c9c9c9}
.footer-nav{position:absolute;left:171px;top:15px;font-size:12px;color:var(--white);display:flex;gap:0}
.footer-nav a{padding:0 14px;border-left:1px solid #cfcfcf;line-height:12px}
.footer-nav a:first-child{padding-left:0;border-left:0}
.copyright{position:absolute;left:171px;top:37px;font-size:12px;color:var(--lime)}
.footer-brand{position:absolute;left:812px;top:15px;display:flex;align-items:center;gap:10px}
.footer-brand .brand-mark{width:30px;height:30px}
.footer-brand .brand-name{font-size:21px;letter-spacing:2px;color:var(--white)}
</style>
</head>
<body>

<header class="site-header">
  <a class="brand" href="#">
    <span class="brand-mark"></span>
    <span class="brand-name">Kestrel Electrical</span>
  </a>
  <a class="connect" href="#" aria-label="Connect with us on palsphere">
    <span>CONNECT WITH US</span>
    <span class="connect-dot"></span>
  </a>
  <form class="search">
    <span class="search-field">Enter Your Keywords Here...</span>
    <span class="search-button">
      <svg width="20" height="20" viewBox="0 0 20 20"><circle cx="8" cy="8" r="6" fill="none" stroke="#fff" stroke-width="2.4"/><line x1="12.5" y1="12.5" x2="18" y2="18" stroke="#fff" stroke-width="3" stroke-linecap="round"/></svg>
    </span>
  </form>
</header>

<nav class="main-nav">
  <a class="current" href="#">HOME</a>
  <a href="#" style="left:315px">ABOUT US</a>
  <span class="nav-sep" style="left:414px"></span>
  <a href="#" style="left:429px">OUR SERVICES</a>
  <span class="nav-sep" style="left:551px"></span>
  <a href="#" style="left:581px">GALLERY</a>
  <span class="nav-sep" style="left:671px"></span>
  <a href="#" style="left:684px">CONTACT US</a>
</nav>

<h1 class="headline"><span class="light">THE NEWEST </span><strong>TECHNOLOGY AT ITS BEST</strong></h1>

<div class="hero" role="img" aria-label="Photo of a ceiling with a custom arrangement of white LED tube lights"></div>

<section class="features">
  <a class="feature" href="#" style="left:172px">
    <div class="feature-photo" role="img" aria-label="Photo of kitchen kickers lit with blue LED strips" style="top:0;height:119px;background:linear-gradient(180deg,#3c4150,#1b2a7a 65%,#6b5a49)"></div>
    <span class="play" style="left:179px;top:13px"></span>
    <div class="feature-caption" style="top:119px;height:50px">Flashing LED strip lighting to kitchen kickers</div>
  </a>
  <a class="feature" href="#" style="left:387px">
    <div class="feature-title">Stair Lights</div>
    <div class="feature-photo" role="img" aria-label="Photo of stairs lit with green LED strips" style="top:50px;height:119px;background:linear-gradient(180deg,#2f7a3e,#4fc35a 55%,#1f6a2c)"></div>
    <span class="play" style="left:171px;top:133px"></span>
  </a>
  <a class="feature" href="#" style="left:600px">
    <div class="feature-photo" role="img" aria-label="Photo of a pendant lamp with a warm bulb" style="top:0;height:119px;background:linear-gradient(90deg,#5a4a3c 0,#4a4d50 12%,#6a6d70 60%,#5a5d60)"></div>
    <span class="play" style="left:177px;top:13px"></span>
    <div class="feature-caption" style="top:119px;height:50px">Custom Led strip Lighting</div>
  </a>
  <a class="feature" href="#" style="left:814px">
    <div class="feature-title">More Custom Lights</div>
    <div class="feature-photo" role="img" aria-label="Photo of timber ceiling beams with warm concealed lighting" style="top:50px;height:119px;background:linear-gradient(180deg,#cfc59a,#8e8c80 60%,#6e6e70)"></div>
    <span class="play" style="left:179px;top:133px"></span>
  </a>
</section>

<footer class="site-footer">
  <nav class="footer-nav">
    <a href="#">HOME</a>
    <a href="#">CONTACT US</a>
    <a href="#">FEEDBACK</a>
    <a href="#">SITEMAP</a>
  </nav>
  <p class="copyright">© 2013 kestrelelectrical.com.au All rights reserved.</p>
  <div class="footer-brand">
    <span class="brand-mark"></span>
    <span class="brand-name">KESTREL</span>
  </div>
</footer>

</body>
</html>
```